Header Graphic for the Westvale TORN Council Website

I need a professionally designed header graphic for a client's site that I've been building for a while now. The site hosts information for a yearly conference for first responders. I'm looking for a rather elegant header with a fixed size of 990x125 and a bit of impact (not overdone though).

I'm attaching some existing artwork to be used.

Color scheme can be seen at https://wvtorn.org.

I've attached a screen shot of the existing site for reference in case you can't access the domain.

Building

Serif
Sans Serif

```html
<!DOCTYPE html>
<html lang="en">
<head>
<meta charset="utf-8">
<title>Westvale TORN Council Training Center</title>
<link rel="stylesheet" href="https://fonts.googleapis.com/css2?family=Open+Sans:wght@300;700&display=swap">
<style>
  :root {
    --band-green: #1f8a40;
    --band-green-dark: #16692f;
    --band-highlight: #7cc98a;
    --room-dark: #1c1f24;
    --room-mid: #3d4450;
    --room-warm: #8a6f5e;
    --shirt-blue: #5d7aa6;
    --table-white: #d9dadc;
    --floor-dark: #1a1c1c;
    --badge-white: #ffffff;
    --badge-green: #1e7a3a;
    --text-white: #ffffff;
  }
  html, body {
    margin: 0;
    padding: 0;
    width: 1200px;
    height: 152px;
    overflow: hidden;
    background: #ffffff;
  }
  .site-header {
    position: relative;
    width: 1200px;
    height: 152px;
    overflow: hidden;
    font-family: "Open Sans", Arial, sans-serif;
    background: var(--floor-dark);
  }
  .audience-photo {
    position: absolute;
    left: 0;
    top: 0;
    width: 1200px;
    height: 101px;
    background:
      radial-gradient(ellipse 90px 45px at 700px 70px, rgba(93,122,166,0.85) 0%, transparent 100%),
      radial-gradient(ellipse 70px 40px at 540px 60px, rgba(110,90,140,0.7) 0%, transparent 100%),
      radial-gradient(ellipse 60px 35px at 1000px 62px, rgba(140,60,70,0.6) 0%, transparent 100%),
      radial-gradient(ellipse 60px 30px at 400px 45px, rgba(138,111,94,0.7) 0%, transparent 100%),
      radial-gradient(ellipse 50px 28px at 720px 28px, rgba(170,140,120,0.65) 0%, transparent 100%),
      radial-gradient(ellipse 45px 25px at 830px 35px, rgba(150,125,110,0.55) 0%, transparent 100%),
      linear-gradient(180deg, transparent 0%, transparent 38%, rgba(217,218,220,0.55) 55%, rgba(217,218,220,0.35) 72%, transparent 88%),
      linear-gradient(90deg, var(--room-mid) 0%, var(--room-dark) 30%, var(--room-mid) 55%, var(--room-warm) 75%, var(--room-mid) 100%),
      var(--room-dark);
  }
  .title-band {
    position: absolute;
    left: 0;
    top: 101px;
    width: 1200px;
    height: 30px;
    background: linear-gradient(180deg, var(--band-green) 0%, var(--band-green-dark) 100%);
    border-top: 2px solid var(--band-highlight);
    box-sizing: border-box;
  }
  .title-band__text {
    position: absolute;
    right: 50px;
    top: 0;
    margin: 0;
    font-weight: 300;
    font-size: 20px;
    line-height: 28px;
    letter-spacing: 0.8px;
    color: var(--text-white);
    text-transform: uppercase;
    white-space: nowrap;
  }
  .brand-badge {
    position: absolute;
    left: 56px;
    top: -2px;
    width: 150px;
    height: 150px;
    border-radius: 50%;
    background: var(--badge-white);
    display: flex;
    align-items: center;
    justify-content: center;
  }
  .brand-badge__name {
    margin: 0;
    font-weight: 700;
    font-size: 17px;
    line-height: 20px;
    text-align: center;
    text-transform: uppercase;
    color: var(--badge-green);
  }
</style>
</head>
<body>
  <header class="site-header">
    <div class="audience-photo" role="img" aria-label="Photo of conference attendees seated at white-clothed tables listening to a presentation"></div>
    <div class="title-band">
      <h1 class="title-band__text">Westvale TORN Council Training Center</h1>
    </div>
    <div class="brand-badge">
      <p class="brand-badge__name">Westvale<br>TORN<br>Council</p>
    </div>
  </header>
</body>
</html>
```